HVRT LLP website - revamping our website after 23 years

Our website needs a complete overhaul. The purpose of this exercise is to provide us with your vision of what you think the website should look like. We don't need the website to be created or coded. Just need creative designs.

We have a four sites that we would like to base our website on;

We like the simplicity of Ravelstoke, the style of Pemberly Adair and Quillfeather.

http://www.pemberlyadair.example/en/toronto-ontario/
http://www.ravelstoke.example/
vintquillfeather.example
http://www.brindlemoor.example/our-professionals.html

We have a logo that we would like to use which will be attached below. We need to keep our website looking very professional as we have a large number of high net worth clients.
Updates

Hi, We've received some good website designs but they appear to be the same type of template websites we've received in the past - this is not what we're looking for. What we want is a unique website that is modelled on the following three company websites: http://www.ravelstoke.example/ www.vintquillfeather.example/ http://www.pemberlyadair.example/en/toronto-ontario/

Thank you everyone for your designs. I will be posting updates and my comments on the various designs in the next day - I want to thank you for the creative designs I see. I thought i would explain a bit about our firm and perhaps it can help when you design the theme of our website: - Our firm is like a family and our clients are truly like our friends. We have close knit relationships in and outside of the office with staff and clients. - We are an 'out of the box' type of firm. We operate differently than most firms and that's a differentiating factor in what makes us who we are - Our slogan is "Count on us" which is a testament to the way we run our practice - We would like an open, fresh, clean look to our website - we don't want the landing page to be overly long or complex because we have limited time to update the website and limited content That's it for the time being - when things come to mind I will post them here.

Can we try a design as follows: - make the website look very similar to www.ravelstoke.example - use the same background colour - Keep the same black top but insert our logo - incorporate some of the content from our current website www.hvrt-ca.example

I have been away dealing with a personal matter. I will look into these websites tomorrow afternoon and provide more feedback / info on the top designer. Thank you

Hi designers, I want to apologize for the delay. I plan on wrapping things up within the next few days. I will go through a few of the top designs and offer my comments. Thank you for your patience.

Target Market(s)

Mainly our current clients - We have a large number of high net worth individuals as clients.

Industry/Entity Type

Accounting

Number of Pages Required

1 page

Requirements
Must have
• Please model website on the websites indicated above.
• Our current website is www.hvrt-ca.example. It's dark, cluttered and not inviting. We want a fresh, clean website. Please incorporate the logo's attached below.

```html
<!DOCTYPE html>
<html lang="en">
<head>
<meta charset="utf-8">
<title>HVRT LLP — Chartered Professional Accountants</title>
<link rel="stylesheet" href="https://fonts.googleapis.com/css2?family=Merriweather:wght@400;700&family=Source+Sans+3:wght@400;600&display=swap">
<style>
:root{
  --ink:#1b1b1b;
  --header-top:#2a2a2a;
  --header-bottom:#050505;
  --header-text:#f2f2f2;
  --header-muted:#9a9a9a;
  --accent-plum:#9b1e63;
  --accent-green:#8cc63f;
  --body-text:#555;
  --footer-link:#777;
  --rule:#d9d9d9;
  --serif:'Merriweather', Georgia, serif;
  --sans:'Source Sans 3', Arial, sans-serif;
}
*{margin:0;padding:0;box-sizing:border-box}
html,body{width:1200px;height:925px;overflow:hidden;background:#fff}
body{position:relative;font-family:var(--sans);color:var(--ink)}

.site-header{position:absolute;left:0;top:0;width:1200px;height:122px;background:linear-gradient(#262626,#0a0a0a)}
.brand{position:absolute;left:74px;top:18px;display:flex;align-items:center;gap:14px}
.brand-mark{width:70px;height:70px;background:var(--accent-plum)}
.brand-name{font-family:var(--serif);font-size:36px;color:#fff;line-height:1}
.brand-tag{position:absolute;left:176px;top:77px;font-family:var(--serif);font-size:8px;color:#fff;letter-spacing:.3px;white-space:nowrap}

.contact-strip{position:absolute;top:18px;display:flex;gap:8px;align-items:center}
.contact-strip svg{stroke:var(--header-muted);fill:none;stroke-width:1.4}
.contact-label{font-family:var(--serif);font-size:13px;color:var(--header-muted);line-height:18px}
.contact-value{font-family:var(--serif);font-size:13px;color:#fff;font-weight:700;line-height:18px}

.main-nav{position:absolute;right:74px;top:72px;width:646px;border-top:1px solid #2d2d2d;display:flex;justify-content:space-between;padding-top:16px}
.main-nav a{font-family:var(--serif);font-size:13.5px;color:#8f8f8f;text-decoration:none;letter-spacing:-.2px}

.hero{position:absolute;left:0;top:122px;width:1200px;height:627px;overflow:hidden}
.hero-photo{position:absolute;inset:0;background:linear-gradient(100deg,#eef0f2 0%,#dfe3e8 38%,#9fa9b8 58%,#4a5670 78%,#2a3550 100%)}
.search{position:absolute;left:884px;top:20px;width:242px;height:30px;background:rgba(255,255,255,.85);font-size:15px;color:#555;padding:6px 10px}
.search svg{position:absolute;right:7px;top:7px}

.hero-lead{position:absolute;left:74px;top:100px;font-family:var(--serif);color:#111}
.hero-lead .strong{font-size:29px;font-weight:700}
.hero-lead .regular{font-size:20px}
.hero-lead .big-num{font-size:36px;font-style:italic;color:var(--accent-plum);font-weight:700}
.hero-lead .years{font-size:20px;color:var(--accent-plum);font-weight:700}
.hero-lead .line2{font-size:20px;display:block;margin-top:-2px}

.devices{position:absolute;left:74px;top:234px;width:395px;height:147px;background:linear-gradient(90deg,#3a3a3a,#e7e1d8 40%,#7fb88a 70%,#2a2a2a)}
.slogan{position:absolute;left:343px;top:262px;font-family:var(--serif);font-size:20px;color:var(--accent-green)}
.hero-rule{position:absolute;left:74px;top:381px;width:810px;border-top:1px solid rgba(255,255,255,.9)}

.feature-cards{position:absolute;left:74px;top:411px;display:flex}
.card{width:270px;height:216px;padding:18px 19px}
.card:nth-child(1){background:rgba(255,255,255,.85)}
.card:nth-child(2){background:rgba(255,255,255,.72)}
.card:nth-child(3){background:rgba(255,255,255,.6)}
.card h2{font-family:var(--serif);font-size:21px;font-weight:700;color:#333;line-height:26px}
.card h3{font-family:var(--serif);font-size:15px;font-weight:400;color:#222;margin-top:3px;padding-bottom:12px;border-bottom:1px solid var(--rule)}
.card p{font-size:15px;line-height:22px;color:var(--body-text);margin-top:13px}
.card a{display:block;margin-top:16px;font-size:13px;color:#111;text-decoration:none}

.slider-tab{position:absolute;left:1010px;top:593px}

.site-footer{position:absolute;left:0;top:749px;width:1200px}
.footer-col{position:absolute;top:34px}
.footer-col h4{font-family:var(--serif);font-size:13.5px;font-weight:400;color:#333;letter-spacing:-.3px;margin-bottom:10px}
.footer-col li{list-style:none;font-size:13px;color:var(--footer-link);line-height:18.5px}
</style>
</head>
<body>
<header class="site-header">
  <div class="brand"><span class="brand-mark"></span><span class="brand-name">HVRT LLP</span></div>
  <div class="brand-tag">CHARTERED PROFESSIONAL ACCOUNTANTS</div>

  <div class="contact-strip" style="left:532px">
    <svg width="30" height="30" viewBox="0 0 30 30"><circle cx="15" cy="15" r="13"/><path d="M15 7v8l5 4"/></svg>
    <div><div class="contact-label">Hours of Operation</div><div class="contact-value">9.00am to 5:00pm</div></div>
  </div>
  <div class="contact-strip" style="left:777px">
    <svg width="30" height="30" viewBox="0 0 30 30"><path d="M6 4l5 0 2 6-3 3c2 4 4 6 8 8l3-3 6 2v5c-12 1-22-9-21-21z"/><path d="M18 5a8 8 0 0 1 7 7M18 9a4 4 0 0 1 3 3"/></svg>
    <div><div class="contact-label">Call Us</div><div class="contact-value">(416) 555-0142</div></div>
  </div>
  <div class="contact-strip" style="left:984px">
    <svg width="32" height="30" viewBox="0 0 32 30"><rect x="2" y="9" width="28" height="19"/><path d="M2 9l14 11 14-11M2 28l10-10M30 28l-10-10M8 9l8-6 8 6"/></svg>
    <div><div class="contact-label">Email Us</div><div class="contact-value">info@hvrt-ca.example</div></div>
  </div>

  <nav class="main-nav">
    <a href="#">HOME</a><a href="#">ABOUT HVRT</a><a href="#">SERVICES</a><a href="#">LIBRARY</a><a href="#">LINKS</a><a href="#">CAREERS</a><a href="#">CONTACT US</a>
  </nav>
</header>

<section class="hero">
  <div class="hero-photo" role="img" aria-label="Photo of an accountant in suit and glasses reviewing documents"></div>
  <div class="search">Search
    <svg width="17" height="17" viewBox="0 0 17 17" fill="none" stroke="#111" stroke-width="2"><circle cx="7" cy="7" r="5.5"/><path d="M11 11l5 5"/></svg>
  </div>

  <div class="hero-lead">
    <span class="strong">Together</span><span class="regular">, We bring over </span>
    <span class="big-num">100</span> <span class="years">Years</span><span class="regular"> of</span>
    <span class="line2">Valuable Experience to the pratice of public accounting</span>
  </div>

  <div class="devices" role="img" aria-label="Laptop, tablet and phone showing the client dashboard"></div>
  <div class="slogan">Count on us !</div>
  <div class="hero-rule"></div>

  <div class="feature-cards">
    <article class="card">
      <h2>2015 Tax Estimator</h2>
      <h3>For 2014 Now Online!</h3>
      <p>Lorem ipsum dolor sit amet, consectetuer adipiscing elit, sed aliquam erat volutpat. Ut wisi enim ...</p>
      <a href="#">[READ MORE]</a>
    </article>
    <article class="card">
      <h2>HVRT Tax Tips</h2>
      <h3>Tax Exemption For Scholarships!</h3>
      <p>Lorem ipsum dolor sit amet, consectetuer adipiscing elit, sed aliquam erat volutpat. Ut wisi enim ...</p>
      <a href="#">[READ MORE]</a>
    </article>
    <article class="card">
      <h2>Why We Are Different</h2>
      <h3>For 2014 Now Online!</h3>
      <p>Lorem ipsum dolor sit amet, consectetuer adipiscing elit, sed aliquam erat volutpat. Ut wisi enim ...</p>
      <a href="#">[READ MORE]</a>
    </article>
  </div>

  <svg class="slider-tab" width="94" height="34" viewBox="0 0 94 34">
    <path d="M0 34c10 0 12-8 16-18C20 5 26 0 36 0h22c10 0 16 5 20 16 4 10 6 18 16 18z" fill="#fff"/>
    <path d="M42 10l-6 7 6 7M52 10l6 7-6 7" fill="none" stroke="#555" stroke-width="2"/>
  </svg>
</section>

<footer class="site-footer">
  <div class="footer-col" style="left:73px">
    <h4>CONTACT US</h4>
    <ul><li>Feedback</li><li>Directions</li><li>Hours of Operation</li><li>Contact an Individual</li></ul>
  </div>
  <div class="footer-col" style="left:253px">
    <h4>ABOUT US</h4>
    <ul><li>Who We Are</li><li>Why We Are Different</li><li>Partner Information</li><li>Staff Profiles</li></ul>
  </div>
  <div class="footer-col" style="left:434px">
    <h4>CAREERS</h4>
    <ul><li>Career Opportunities at HVRT</li><li>E-Mail Us</li></ul>
  </div>
  <div class="footer-col" style="left:701px">
    <h4 style="margin-left:2px">LOGIN</h4>
    <ul><li>@HVRT LLP</li><li>All Rights Reserved</li></ul>
  </div>
</footer>
</body>
</html>
```